Business Card Design for Small Electrical Contractor

I need to update my business card into something a little more modern. We are a small electrical contracting company. We service domestic and commercial places around Sydney. We have 2 logo designs at the moment. I have uploaded both and 2 different sizes to work with.

Industry/Entity Type

Business

Contact Information for Business Card

Leo Hartigan
8/21-23 Birch Rd, Kelsworth 2087
t - (02) 9381 4720
m - 0427 815 903
E - info@hartiganelx.com.au
W - hartiganelx.com.au
ABN: 42 907 551 316

Font styles to use
Sans Serif

Requirements
Must have
• I would also like to see the below fit on somewhere aswell
• - Licensed Electrician
• - Level 2 (Cat 1 & 4)
• - Domestic
• - Commercial
• - Repairs and Installations
• - Data
Nice to have
• Try and keep similar colours as logo
Should not have
• No lightning bolts or light globes. Smart and professional please.

```html
<!DOCTYPE html>
<html lang="en">
<head>
<meta charset="utf-8">
<title>Hartigan Electrical – Business Cards</title>
<link rel="stylesheet" href="https://fonts.googleapis.com/css2?family=Lato:wght@400;700&display=swap">
<style>
  :root {
    --bg: #e6e8ea;
    --green: #12373a;
    --orange: #f7941d;
    --white: #ffffff;
    --ink: #12373a;
  }
  html, body {
    margin: 0;
    padding: 0;
    width: 1200px;
    height: 898px;
    overflow: hidden;
    background: var(--bg);
    font-family: "Lato", Arial, sans-serif;
  }
  .canvas {
    position: relative;
    width: 1200px;
    height: 898px;
  }
  .card {
    position: absolute;
    width: 600px;
    height: 366px;
    overflow: hidden;
    box-shadow: 0 8px 22px rgba(0,0,0,0.18);
  }

  /* Front */
  .card-front {
    left: 150px;
    top: 60px;
    background: var(--green);
    color: var(--white);
  }
  .card-front .brand {
    position: absolute;
    left: 0;
    right: 0;
    top: 118px;
    text-align: center;
  }
  .brand-name {
    font-weight: 700;
    font-size: 46px;
    letter-spacing: 0.5px;
    line-height: 1;
  }
  .card-front .brand-name { color: var(--white); }
  .brand-rule {
    width: 330px;
    height: 3px;
    margin: 18px auto 0;
    background: var(--orange);
  }
  .services {
    position: absolute;
    left: 0;
    right: 0;
    bottom: 44px;
    margin: 0;
    text-align: center;
    font-size: 16px;
    letter-spacing: 0.8px;
    line-height: 1.45;
  }
  .services .dot { color: var(--orange); padding: 0 6px; }

  /* Back */
  .card-back {
    left: 450px;
    top: 476px;
    background: var(--white);
  }
  .card-back .wave {
    position: absolute;
    inset: 0;
    width: 600px;
    height: 366px;
  }
  .card-back .brand {
    position: absolute;
    left: 44px;
    top: 72px;
  }
  .card-back .brand-name {
    color: var(--ink);
    font-size: 30px;
  }
  .card-back .brand-rule {
    width: 210px;
    height: 2px;
    margin: 10px 0 0;
  }
  .person {
    position: absolute;
    right: 46px;
    top: 20px;
    color: var(--ink);
  }
  .person-name { font-size: 22px; line-height: 1.2; }
  .person-role { font-size: 15px; margin-top: 2px; }
  .address {
    position: absolute;
    left: 50px;
    bottom: 34px;
    margin: 0;
    color: var(--white);
    font-size: 17px;
    line-height: 1.35;
  }
  .contacts {
    position: absolute;
    left: 330px;
    bottom: 30px;
    margin: 0;
    padding: 0;
    list-style: none;
    color: var(--white);
    font-size: 17px;
    line-height: 1.5;
  }
  .contacts li { display: flex; align-items: center; gap: 12px; }
  .contacts svg { width: 15px; height: 15px; flex: none; fill: var(--orange); }
</style>
</head>
<body>
<main class="canvas">

  <section class="card card-front" aria-label="Business card front">
    <div class="brand">
      <div class="brand-name">Hartigan Electrical</div>
      <div class="brand-rule"></div>
    </div>
    <p class="services">
      Licensed Electrician<span class="dot">•</span>Level 2 (Cat 1 &amp; 4)<span class="dot">•</span>Domestic<br>
      Commercial<span class="dot">•</span>Repairs and Installations<span class="dot">•</span>Data
    </p>
  </section>

  <section class="card card-back" aria-label="Business card back">
    <svg class="wave" viewBox="0 0 600 366" aria-hidden="true">
      <path d="M0 205 C110 212 210 205 300 165 S480 110 600 100 L600 366 L0 366 Z" fill="var(--orange)"/>
      <path d="M0 242 C110 248 220 240 310 200 S490 148 600 140 L600 366 L0 366 Z" fill="var(--green)" stroke="var(--white)" stroke-width="3"/>
    </svg>

    <div class="person">
      <div class="person-name">Leo Hartigan</div>
      <div class="person-role">Owner</div>
    </div>

    <div class="brand">
      <div class="brand-name">Hartigan Electrical</div>
      <div class="brand-rule"></div>
    </div>

    <p class="address">8/21-23 Birch Rd<br>Kelsworth 2087</p>

    <ul class="contacts">
      <li>
        <svg viewBox="0 0 24 24"><path d="M6.6 10.8a15.1 15.1 0 0 0 6.6 6.6l2.2-2.2a1 1 0 0 1 1-.25 11.4 11.4 0 0 0 3.6.57 1 1 0 0 1 1 1V20a1 1 0 0 1-1 1A17 17 0 0 1 3 4a1 1 0 0 1 1-1h3.5a1 1 0 0 1 1 1c0 1.25.2 2.45.57 3.57a1 1 0 0 1-.25 1z"/></svg>
        (02) 9381 4720
      </li>
      <li>
        <svg viewBox="0 0 24 24"><path d="M7 1h10a2 2 0 0 1 2 2v18a2 2 0 0 1-2 2H7a2 2 0 0 1-2-2V3a2 2 0 0 1 2-2zm0 3v14h10V4zm5 15.5a1.2 1.2 0 1 0 0 2.4 1.2 1.2 0 0 0 0-2.4z"/></svg>
        0427 815 903
      </li>
      <li>
        <svg viewBox="0 0 24 24"><path d="M2 5h20v14H2zm2 2v.5l8 5 8-5V7zm0 2.8V17h16V9.8l-8 5z"/></svg>
        info@hartiganelx.com.au
      </li>
      <li>
        <svg viewBox="0 0 24 24"><path d="M12 2a10 10 0 1 0 0 20 10 10 0 0 0 0-20zm6.9 9h-3a15 15 0 0 0-1.3-5.6A8 8 0 0 1 18.9 11zM12 4.1c.9 1.2 1.8 3.6 1.9 6.9h-3.8c.1-3.3 1-5.7 1.9-6.9zM9.4 5.4A15 15 0 0 0 8.1 11h-3a8 8 0 0 1 4.3-5.6zM5.1 13h3a15 15 0 0 0 1.3 5.6A8 8 0 0 1 5.1 13zm6.9 6.9c-.9-1.2-1.8-3.6-1.9-6.9h3.8c-.1 3.3-1 5.7-1.9 6.9zm2.6-1.3a15 15 0 0 0 1.3-5.6h3a8 8 0 0 1-4.3 5.6z"/></svg>
        hartiganelx.com.au
      </li>
    </ul>
  </section>

</main>
</body>
</html>
```